Summer Sale Graphics for Social Media

I want to create 11 social media graphics (new Instagram size 4:5 (1080 x 1350 pixels) focusing on our Summer Sale Graphics, using any of the pics attached. Use the attached pics, NO RANDOM STOCK PHOTOGRAPHY. For the color scheme of the graphics, they should all be complementary to the product colors in the photos.
You can add any of the photos attached but none are required. You can do some of the graphics in all text. I mainly need BOLD text that says one of the headlines (11 total) SEE ATTACHED WORD DOCUMENT for the headlines to use.

```html
<!DOCTYPE html>
<html lang="en">
<head>
<meta charset="utf-8">
<title>Summer Sale – Slim Waist, Flat Tummy, More Energy</title>
<link rel="stylesheet" href="https://fonts.googleapis.com/css2?family=Anton&family=Baloo+2:wght@800&family=Montserrat:wght@700&display=swap">
<style>
  :root {
    --navy: #182057;
    --navy-deep: #0e1438;
    --cyan: #1de3e0;
    --cyan-leaf: #17b0b0;
    --pink: #f04aa6;
    --pink-leaf: #c93d8e;
    --orange: #f08224;
    --orange-shadow: #b8621f;
    --white: #ffffff;
    --cloud: #6e7598;
    --teal-text: #3bdcc3;
    --red: #e8102a;
    --shade-pink: #e35cc8;
  }
  html, body {
    margin: 0;
    padding: 0;
    width: 960px;
    height: 1200px;
    overflow: hidden;
    background: var(--navy);
  }
  .poster {
    display: block;
    width: 960px;
    height: 1200px;
  }
  .bg-navy { fill: var(--navy); }
  .bg-cyan { fill: var(--cyan); }
  .bg-pink { fill: var(--pink); }
  .leaf-cyan { fill: var(--cyan-leaf); opacity: 0.75; }
  .leaf-pink { fill: var(--pink-leaf); opacity: 0.75; }
  .ring { fill: none; stroke: var(--white); stroke-width: 5; }
  .cloud { fill: var(--cloud); }
  .banner { fill: var(--orange); stroke: var(--white); stroke-width: 3; }
  .banner-shadow { fill: var(--navy-deep); opacity: 0.8; }
  .headline {
    font-family: "Anton", "Oswald", sans-serif;
    font-size: 128px;
    fill: var(--white);
    text-anchor: middle;
  }
  .headline-shadow {
    font-family: "Anton", "Oswald", sans-serif;
    font-size: 128px;
    fill: var(--orange-shadow);
    text-anchor: middle;
  }
  .cheer {
    font-family: "Baloo 2", "Fredoka", sans-serif;
    font-weight: 800;
    font-size: 150px;
    fill: var(--teal-text);
    text-anchor: middle;
  }
  .cheer-shadow {
    font-family: "Baloo 2", "Fredoka", sans-serif;
    font-weight: 800;
    font-size: 150px;
    fill: var(--navy-deep);
    text-anchor: middle;
  }
  .sale-frame { fill: var(--white); }
  .sale-box { fill: var(--red); }
  .sale-text {
    font-family: "Montserrat", sans-serif;
    font-weight: 700;
    font-size: 92px;
    fill: var(--white);
    text-anchor: middle;
  }
  .sunglasses { fill: var(--shade-pink); opacity: 0.85; }
</style>
</head>
<body>
<svg class="poster" viewBox="0 0 1080 1350" xmlns="http://www.w3.org/2000/svg">
  <!-- background fields -->
  <rect class="bg-navy" x="0" y="0" width="1080" height="1350"/>
  <polygon class="bg-cyan" points="0,0 1080,0 1080,128 0,490"/>
  <polygon class="bg-pink" points="1080,985 1080,1350 262,1350"/>

  <!-- foliage areas -->
  <polygon class="leaf-cyan" role="img" aria-label="Palm leaf silhouettes" points="0,0 560,0 560,150 300,345 0,470"/>
  <polygon class="leaf-pink" role="img" aria-label="Palm leaf silhouettes" points="1080,1060 1080,1350 700,1350 760,1200 900,1080"/>

  <!-- rings -->
  <circle class="ring" cx="895" cy="350" r="255"/>
  <circle class="ring" cx="-25" cy="1200" r="255"/>

  <!-- clouds -->
  <g class="cloud">
    <path d="M968,305 a22,22 0 0 1 28,-30 a32,32 0 0 1 60,-8 a22,22 0 0 1 24,20 v18 z"/>
    <path d="M32,670 a22,22 0 0 1 28,-30 a34,34 0 0 1 64,-8 a24,24 0 0 1 50,38 z"/>
    <path d="M968,842 a22,22 0 0 1 28,-30 a34,34 0 0 1 62,-8 a22,22 0 0 1 22,18 v20 z"/>
    <path d="M15,1210 a26,26 0 0 1 34,-34 a40,40 0 0 1 76,-10 a28,28 0 0 1 60,44 z"/>
  </g>

  <!-- banner shadows -->
  <polygon class="banner-shadow" points="185,330 908,227 900,297 985,420 190,567"/>
  <polygon class="banner-shadow" points="228,577 895,474 908,707 228,777"/>
  <polygon class="banner-shadow" points="62,812 960,722 970,902 77,1020 212,882"/>

  <!-- banners -->
  <polygon class="banner" points="165,308 888,205 880,275 965,398 170,545"/>
  <polygon class="banner" points="208,555 875,452 888,685 208,755"/>
  <polygon class="banner" points="40,790 940,702 950,880 55,998 190,860"/>

  <!-- headlines -->
  <g transform="rotate(-10 535 400)">
    <text class="headline-shadow" x="543" y="453" textLength="585" lengthAdjust="spacingAndGlyphs">SLIM WAIST</text>
    <text class="headline" x="535" y="445" textLength="585" lengthAdjust="spacingAndGlyphs">SLIM WAIST</text>
  </g>
  <g transform="rotate(-10 548 645)">
    <text class="headline-shadow" x="556" y="698" textLength="625" lengthAdjust="spacingAndGlyphs">FLAT TUMMY</text>
    <text class="headline" x="548" y="690" textLength="625" lengthAdjust="spacingAndGlyphs">FLAT TUMMY</text>
  </g>
  <g transform="rotate(-8 562 850)">
    <text class="headline-shadow" x="570" y="903" textLength="715" lengthAdjust="spacingAndGlyphs">MORE ENERGY</text>
    <text class="headline" x="562" y="895" textLength="715" lengthAdjust="spacingAndGlyphs">MORE ENERGY</text>
  </g>

  <!-- sunglasses -->
  <rect class="sunglasses" role="img" aria-label="Pink sunglasses sticker" x="705" y="130" width="250" height="85" rx="38" transform="rotate(12 830 172)"/>

  <!-- cheer line -->
  <g transform="rotate(-8 575 1040)">
    <text class="cheer-shadow" x="583" y="1098" textLength="600" lengthAdjust="spacingAndGlyphs">Let’s Go!</text>
    <text class="cheer" x="575" y="1090" textLength="600" lengthAdjust="spacingAndGlyphs">Let’s Go!</text>
  </g>

  <!-- call to action -->
  <rect class="sale-frame" x="393" y="1140" width="642" height="136"/>
  <rect class="sale-box" x="405" y="1151" width="618" height="114"/>
  <text class="sale-text" x="719" y="1242" textLength="560" lengthAdjust="spacingAndGlyphs">SALE NOW!</text>
</svg>
</body>
</html>
```